Garage Door Business Truck Wrap

looking to create a wrap for a 2012 varnel tallhorn 3400 XT single cab with service bed. please use creativity, here is the website www.bluefernliftdoorsvc.com.. Also, I will upload documents of branded items, Id like everything to seamlessly flow together

```html
<!DOCTYPE html>
<html lang="en">
<head>
<meta charset="utf-8">
<title>Bluefern Lift – Service Truck Wrap Concepts</title>
<link href="https://fonts.googleapis.com/css2?family=Cinzel:wght@500&family=Oswald:wght@500;700&display=swap" rel="stylesheet">
<style>
  :root {
    --paper: #ffffff;
    --wrap-black: #0c0b0a;
    --wrap-gold: #b0924a;
    --gold-deep: #8d7332;
    --gold-light: #d2b46a;
    --glass: #3a3d42;
    --hood-white: #e9e9e6;
    --ink: #1a1710;
  }
  * { margin: 0; padding: 0; box-sizing: border-box; }
  html, body { width: 1200px; height: 1200px; overflow: hidden; background: var(--paper); }
  .concept-stack {
    position: absolute; left: 309px; top: 22px; width: 582px;
    display: flex; flex-direction: column; gap: 14px;
  }
  .wrap-concept { width: 582px; height: 280px; display: block; }
  .brand-name { font-family: "Cinzel", serif; font-weight: 500; fill: var(--gold-light); letter-spacing: 1.5px; }
  .brand-tagline { font-family: "Cinzel", serif; fill: var(--gold-light); letter-spacing: 2px; }
  .credential { font-family: "Oswald", sans-serif; font-weight: 500; fill: var(--gold-light); }
  .web-address { font-family: "Oswald", sans-serif; font-weight: 500; fill: var(--ink); }
  .phone-number { font-family: "Oswald", sans-serif; font-weight: 700; fill: var(--ink); letter-spacing: 1px; }
  .service-hours { font-family: "Oswald", sans-serif; font-weight: 700; fill: #ffffff; }
  .cab-body { fill: var(--wrap-black); }
  .cab-glass { fill: var(--glass); }
  .bed-body { fill: var(--wrap-gold); }
  .bed-accent { fill: var(--wrap-black); }
  .web-band { fill: var(--wrap-gold); }
  .gold-stripe { fill: var(--wrap-gold); }
  .hood-panel { fill: var(--hood-white); }
  .door-panel { fill: var(--gold-deep); opacity: .55; }
  .wheel-well { fill: var(--paper); }
</style>
</head>
<body>
<main class="concept-stack">

  <!-- Concept A -->
  <svg class="wrap-concept" viewBox="0 0 582 280" aria-label="Wrap concept A">
    <path class="cab-body" d="M8 200 L8 118 L40 100 L150 92 L175 50 L300 46 L300 215 L8 215 Z"/>
    <path class="cab-glass" d="M185 58 L236 56 L236 104 L165 104 Z"/>
    <rect class="bed-body" x="306" y="84" width="268" height="131"/>
    <path class="bed-accent" d="M306 84 L410 84 L410 120 Q380 190 306 190 Z"/>
    <rect class="web-band" x="120" y="170" width="180" height="16"/>
    <text class="credential" x="20" y="134" font-size="10">LICENSED AND INSURED</text>
    <text class="brand-name" x="192" y="148" font-size="15" text-anchor="middle">BLUEFERN LIFT</text>
    <text class="brand-tagline" x="192" y="160" font-size="6" text-anchor="middle">DOORS AND OPENERS</text>
    <text class="web-address" x="210" y="182" font-size="9" text-anchor="middle">www.bluefernliftdoorsvc.com</text>
    <text class="phone-number" x="488" y="128" font-size="17" text-anchor="middle">(555) 214-0386</text>
    <text class="service-hours" x="548" y="184" font-size="10" text-anchor="middle">24/7</text>
    <text class="service-hours" x="548" y="194" font-size="6" text-anchor="middle">Emergency Services</text>
    <circle class="wheel-well" cx="90" cy="225" r="40"/>
    <circle class="wheel-well" cx="440" cy="225" r="40"/>
  </svg>

  <!-- Concept B -->
  <svg class="wrap-concept" viewBox="0 0 582 280" aria-label="Wrap concept B">
    <path class="cab-body" d="M8 200 L8 118 L40 100 L150 92 L175 50 L300 46 L300 215 L8 215 Z"/>
    <path class="cab-glass" d="M185 58 L236 56 L236 104 L165 104 Z"/>
    <rect class="bed-body" x="306" y="84" width="268" height="131"/>
    <path class="bed-accent" d="M306 84 L410 84 L410 120 Q380 190 306 190 Z"/>
    <rect class="web-band" x="120" y="170" width="180" height="16"/>
    <text class="credential" x="20" y="134" font-size="10">LICENSED AND INSURED</text>
    <text class="brand-name" x="192" y="148" font-size="15" text-anchor="middle">BLUEFERN LIFT</text>
    <text class="brand-tagline" x="192" y="160" font-size="6" text-anchor="middle">DOORS AND OPENERS</text>
    <text class="web-address" x="210" y="182" font-size="9" text-anchor="middle">www.bluefernliftdoorsvc.com</text>
    <text class="phone-number" x="480" y="110" font-size="17" text-anchor="middle">(555) 214-0386</text>
    <text class="service-hours" x="548" y="168" font-size="10" text-anchor="middle">24/7</text>
    <text class="service-hours" x="548" y="178" font-size="6" text-anchor="middle">Emergency Services</text>
    <circle class="wheel-well" cx="90" cy="225" r="40"/>
    <circle class="wheel-well" cx="440" cy="225" r="40"/>
  </svg>

  <!-- Concept C -->
  <svg class="wrap-concept" viewBox="0 0 582 280" aria-label="Wrap concept C">
    <path class="cab-body" d="M8 200 L8 118 L40 100 L150 92 L175 50 L300 46 L300 215 L8 215 Z"/>
    <path class="cab-glass" d="M185 58 L236 56 L236 104 L165 104 Z"/>
    <path class="gold-stripe" d="M286 110 L300 95 L300 160 L262 200 L240 200 Z"/>
    <rect class="bed-body" x="306" y="84" width="268" height="131"/>
    <rect class="door-panel" x="318" y="112" width="210" height="70" role="img" aria-label="Garage door panel pattern"/>
    <rect class="web-band" x="110" y="168" width="150" height="16"/>
    <text class="credential" x="20" y="134" font-size="10">LICENSED AND INSURED</text>
    <text class="brand-name" x="185" y="148" font-size="15" text-anchor="middle">BLUEFERN LIFT</text>
    <text class="brand-tagline" x="185" y="160" font-size="6" text-anchor="middle">DOORS AND OPENERS</text>
    <text class="web-address" x="185" y="180" font-size="9" text-anchor="middle">www.bluefernliftdoorsvc.com</text>
    <text class="phone-number" x="430" y="108" font-size="18" text-anchor="middle">(555) 214-0386</text>
    <text class="service-hours" x="548" y="168" font-size="10" text-anchor="middle">24/7</text>
    <text class="service-hours" x="548" y="178" font-size="6" text-anchor="middle">Emergency Services</text>
    <circle class="wheel-well" cx="90" cy="225" r="40"/>
    <circle class="wheel-well" cx="440" cy="225" r="40"/>
  </svg>

  <!-- Concept D -->
  <svg class="wrap-concept" viewBox="0 0 582 280" aria-label="Wrap concept D">
    <path class="cab-body" d="M8 200 L8 118 L40 100 L150 92 L175 50 L300 46 L300 215 L8 215 Z"/>
    <path class="hood-panel" d="M8 124 L8 118 L40 100 L150 92 L162 72 L120 112 L40 120 Z"/>
    <path class="cab-glass" d="M185 58 L236 56 L236 104 L165 104 Z"/>
    <path class="gold-stripe" d="M286 110 L300 95 L300 160 L262 200 L240 200 Z"/>
    <rect class="bed-body" x="306" y="84" width="268" height="131"/>
    <rect class="door-panel" x="318" y="112" width="210" height="70" role="img" aria-label="Garage door panel pattern"/>
    <rect class="web-band" x="110" y="168" width="150" height="16"/>
    <text class="credential" x="20" y="134" font-size="10">LICENSED AND INSURED</text>
    <text class="brand-name" x="185" y="148" font-size="15" text-anchor="middle">BLUEFERN LIFT</text>
    <text class="brand-tagline" x="185" y="160" font-size="6" text-anchor="middle">DOORS AND OPENERS</text>
    <text class="web-address" x="185" y="180" font-size="9" text-anchor="middle">www.bluefernliftdoorsvc.com</text>
    <text class="phone-number" x="430" y="108" font-size="18" text-anchor="middle">(555) 214-0386</text>
    <text class="service-hours" x="548" y="168" font-size="10" text-anchor="middle">24/7</text>
    <text class="service-hours" x="548" y="178" font-size="6" text-anchor="middle">Emergency Services</text>
    <circle class="wheel-well" cx="90" cy="225" r="40"/>
    <circle class="wheel-well" cx="440" cy="225" r="40"/>
  </svg>

</main>
</body>
</html>
```